Commercial and Multifamily informational website

We need a website for our commercial real estate management company. We will manage offices, retail, apartments and others. Here is the brief verbiage: Providing quality commercial and multifamily portfolio management to Landlords, REITs, and financial institutions. 

Industry/Entity Type

Real Estate

Number of Pages Required

2 page

Font styles to use
Sans Serif
Other font styles liked:
• Muli, Garamond

Colors
0555a3
5c5c5c
3176b5
85acd3
474747

Requirements
Must have
• Home page and contact page

```html
<!DOCTYPE html>
<html lang="en">
<head>
<meta charset="utf-8">
<title>Kestrel Real Estate Management</title>
<link href="https://fonts.googleapis.com/css2?family=Mulish:wght@400;600;700&family=Lato:wght@400;700&display=swap" rel="stylesheet">
<style>
  :root {
    --blue: #0555a3;
    --blue-mid: #3176b5;
    --blue-light: #85acd3;
    --grey: #5c5c5c;
    --grey-dark: #474747;
    --panel: #f2f2f2;
    --white: #ffffff;
  }
  * { margin: 0; padding: 0; box-sizing: border-box; }
  html, body { width: 830px; height: 1200px; overflow: hidden; background: var(--white); }
  body { position: relative; font-family: "Lato", sans-serif; color: var(--grey-dark); }

  .site-header { position: absolute; left: 0; top: 0; width: 830px; height: 88px; border-bottom: 2px solid var(--blue); }
  .brand { position: absolute; left: 68px; top: 22px; display: flex; align-items: center; gap: 10px; font-family: "Mulish", sans-serif; font-weight: 700; color: var(--blue); }
  .brand-mark { width: 14px; height: 44px; background: var(--blue); }
  .brand-name { font-size: 19px; line-height: 21px; letter-spacing: .3px; }
  .header-contact { position: absolute; right: 66px; top: 17px; display: flex; gap: 12px; font-family: "Mulish", sans-serif; font-size: 11.5px; color: var(--grey-dark); }
  .header-contact span { display: flex; align-items: center; gap: 6px; }
  .main-nav { position: absolute; right: 62px; top: 55px; display: flex; font-family: "Lato", sans-serif; font-size: 11.5px; }
  .main-nav a { display: block; height: 31px; line-height: 31px; padding: 0 13px; color: var(--grey-dark); text-decoration: none; }
  .main-nav a.active { background: var(--blue); color: var(--white); border-radius: 4px 4px 0 0; }

  .hero { position: absolute; left: 0; top: 88px; width: 830px; height: 356px; background: linear-gradient(180deg, #c9d7e6 0%, #8ea6c2 35%, #4b5f7d 70%, #3a4658 100%); }
  .hero-caption { position: absolute; left: 0; bottom: 0; width: 830px; height: 59px; background: rgba(5, 85, 163, .88); color: var(--white); font-family: "Mulish", sans-serif; font-size: 19px; line-height: 22px; text-align: center; padding-top: 8px; }

  .section-title { position: absolute; left: 0; width: 830px; text-align: center; font-family: "Mulish", sans-serif; font-weight: 400; font-size: 28px; color: var(--grey-dark); }
  .section-title em { font-style: normal; color: var(--blue); }
  .divider { position: absolute; left: 367px; width: 96px; height: 6px; border-top: 1px solid #9aa3ad; border-bottom: 1px solid #9aa3ad; }

  .about-lead, .about-body { position: absolute; left: 68px; width: 694px; text-align: center; font-size: 9.4px; line-height: 13.2px; }
  .about-lead { top: 535px; font-weight: 700; color: var(--grey-dark); }
  .about-body { top: 575px; color: var(--grey); }
  .btn { position: absolute; left: 362px; top: 644px; width: 107px; height: 31px; background: var(--blue); color: var(--white); border-radius: 3px; box-shadow: 0 2px 0 var(--blue-mid); font-family: "Mulish", sans-serif; font-size: 10.5px; line-height: 31px; text-align: center; }

  .services { position: absolute; left: 0; top: 711px; width: 830px; height: 284px; background: var(--panel); }
  .service-card { position: absolute; top: 100px; width: 160px; }
  .service-photo { width: 160px; height: 119px; background: var(--white); padding: 4px; box-shadow: 0 6px 6px -4px rgba(0,0,0,.25); }
  .service-photo div { width: 100%; height: 100%; }
  .service-label { margin-top: 14px; text-align: center; font-family: "Mulish", sans-serif; font-size: 14.5px; color: var(--grey-dark); }

  .site-footer { position: absolute; left: 0; top: 995px; width: 830px; height: 175px; background: linear-gradient(90deg, #2a120e 0%, #3d1a12 45%, #2c1410 100%); color: var(--white); }
  .footer-heading { position: absolute; top: 28px; font-family: "Mulish", sans-serif; font-size: 12.5px; padding-bottom: 4px; border-bottom: 1px solid var(--white); }
  .quick-links { position: absolute; left: 68px; top: 65px; list-style: none; font-size: 9.5px; font-weight: 700; }
  .quick-links li { height: 19px; display: flex; align-items: center; gap: 10px; }
  .quick-links li::before { content: ""; width: 4px; height: 4px; border-radius: 50%; background: var(--white); }
  .quick-links li.current { color: var(--blue-mid); }
  .quick-links li.current::before { background: var(--blue-mid); }
  .contact-list { position: absolute; left: 295px; top: 62px; font-size: 9.3px; }
  .contact-row { display: flex; gap: 11px; margin-bottom: 9px; line-height: 14px; }
  .contact-row strong { color: var(--blue-mid); font-weight: 700; }
  .footer-brand { position: absolute; left: 524px; top: 42px; display: flex; align-items: center; gap: 8px; font-family: "Mulish", sans-serif; font-weight: 700; font-size: 17px; line-height: 18px; color: #d8d8d8; }
  .footer-brand .brand-mark { width: 10px; height: 44px; background: #d8d8d8; }
  .social { position: absolute; left: 594px; top: 137px; display: flex; gap: 8px; }
  .social span { width: 19px; height: 19px; border-radius: 50%; border: 2px solid var(--white); }

  .copyright { position: absolute; left: 0; top: 1170px; width: 830px; height: 30px; background: var(--blue); color: var(--white); font-size: 9.5px; line-height: 30px; text-align: center; }
</style>
</head>
<body>
  <header class="site-header">
    <div class="brand"><span class="brand-mark"></span><span class="brand-name">KESTREL<br>REAL ESTATE MANAGEMENT</span></div>
    <div class="header-contact">
      <span><svg width="22" height="22" viewBox="0 0 22 22"><circle cx="11" cy="11" r="10" fill="none" stroke="#0555a3" stroke-width="1.6"/><path d="M7.5 6.5l2 -.5 1 2.5-1.3 1a6 6 0 0 0 3 3l1-1.3 2.5 1-.5 2c-4 .5-8-3.5-7.7-7.7z" fill="#0555a3"/></svg>123-456-7890</span>
      <span><svg width="22" height="22" viewBox="0 0 22 22"><circle cx="11" cy="11" r="10" fill="none" stroke="#0555a3" stroke-width="1.6"/><rect x="6" y="7.5" width="10" height="7" fill="#0555a3"/><path d="M6 7.5l5 4 5-4" fill="none" stroke="#fff" stroke-width="1"/></svg>info@kestrelproperty.com</span>
    </div>
    <nav class="main-nav"><a class="active">Home</a><a>About Us</a><a>Services</a><a>Contact Us</a></nav>
  </header>

  <section class="hero" role="img" aria-label="Modern blue glass office building under a pale sky">
    <div class="hero-caption">Providing Quality Commercial And Multifamily Portfolio<br>Management To Landlords, REITs, And Financial Institutions.</div>
  </section>

  <h1 class="section-title" style="top:472px">About <em>Kestrel Real Estate Management</em></h1>
  <div class="divider" style="top:517px"></div>
  <p class="about-lead">Lorem ipsum dolor sit amet, consectetuer adipiscing elit, sed diam nonummy nibh euismod tincidunt ut laoreet dolore magna aliquam erat volutpat. Ut wisi enim ad minim veniam, quis nostrud exerci tation ullamcorper suscipit lobortis nisl ut aliquip ex ea commodo consequat.</p>
  <p class="about-body">Lorem ipsum dolor sit amet, consectetuer adipiscing elit, sed diam nonummy nibh euismod tincidunt ut laoreet dolore magna aliquam erat volutpat. Ut wisi enim ad minim veniam, quis nostrud exerci tation ullamcorper suscipit lobortis nisl ut aliquip ex ea commodo consequat. Duis autem vel eum iriure dolor in hendrerit in vulputate velit esse molestie consequat, vel illum dolore eu feugiat nulla facilisis at vero eros et accumsan et iusto odio dignissim qui blandit praesent luptatum zzril delenit augue duis dolore te feugait nulla facilisi.</p>
  <div class="btn">Read More</div>

  <section class="services">
    <h2 class="section-title" style="top:29px">Our <em>Services</em></h2>
    <div class="divider" style="top:73px"></div>
    <div class="service-card" style="left:68px"><div class="service-photo"><div role="img" aria-label="Open-plan office with desks and monitors" style="background:linear-gradient(180deg,#e8eaee,#b9bfc6)"></div></div><div class="service-label">Manage Offices</div></div>
    <div class="service-card" style="left:246px"><div class="service-photo"><div role="img" aria-label="Shopper walking through a retail arcade" style="background:linear-gradient(90deg,#6c5a52,#9ea7b2)"></div></div><div class="service-label">Retail</div></div>
    <div class="service-card" style="left:424px"><div class="service-photo"><div role="img" aria-label="Apartment tower against a blue sky" style="background:linear-gradient(180deg,#4f74b5,#c8c2b6)"></div></div><div class="service-label">Apartments</div></div>
    <div class="service-card" style="left:602px"><div class="service-photo"><div role="img" aria-label="Contemporary commercial property at dusk" style="background:linear-gradient(180deg,#3b5f9e,#9aa7a2)"></div></div><div class="service-label">Property</div></div>
  </section>

  <footer class="site-footer" role="img" aria-label="Dimly lit restaurant interior in warm tones">
    <div class="footer-heading" style="left:68px">Quick Links</div>
    <ul class="quick-links"><li class="current">Home</li><li>About Us</li><li>Services</li><li>Contact Us</li></ul>
    <div class="footer-heading" style="left:295px">Contact Us</div>
    <div class="contact-list">
      <div class="contact-row"><svg width="9" height="13" viewBox="0 0 9 13"><path d="M4.5 0a4.5 4.5 0 0 1 4.5 4.5c0 3-4.5 8.5-4.5 8.5S0 7.5 0 4.5A4.5 4.5 0 0 1 4.5 0z" fill="#fff"/><circle cx="4.5" cy="4.5" r="1.6" fill="#3d1a12"/></svg><span><strong>Kestrel Real Estate Management</strong><br>123 Lorem Epsum set Adam</span></div>
      <div class="contact-row"><svg width="11" height="13" viewBox="0 0 11 13"><rect x="0" y="3" width="11" height="7" fill="#fff"/><path d="M0 3l5.5 4 5.5-4" fill="none" stroke="#3d1a12"/></svg>info@kestrelproperty.com</div>
      <div class="contact-row"><svg width="11" height="13" viewBox="0 0 11 13"><path d="M1 2l2.5-.5 1.3 3-1.5 1.2a6 6 0 0 0 3 3l1.2-1.5 3 1.3-.5 2.5C5 11.5.5 7 1 2z" fill="#fff"/></svg>123-465-7890</div>
    </div>
    <div class="footer-brand"><span class="brand-mark"></span><span>KESTREL<br>REAL ESTATE<br>MANAGEMENT</span></div>
    <div class="social"><span style="background:#3b5998"></span><span style="background:#1da1f2"></span><span style="background:#0077b5"></span><span style="background:#dd4b39"></span></div>
  </footer>

  <div class="copyright">Copyright © 2017 Kestrel Real Estate Management. All rights reserved</div>
</body>
</html>
```